Fitness Equipment Repair Business Needs a Catchy New Business Card

We have an existing business card, however, it is quite plain and boring. We are expanding primarily in the commercial area (gyms, studios, apartment complexes etc). The business card will serve as eye candy to those managers/owners that can't be met for a face to face.
Originally I was planning for a brochure as well, but all of our information is better summarized on our website. (brasswheelservicing.ca).
I would like the card to match the colour scheme of the website and utilize the logo. It should have a professional clean feel to it, however, a little colouring outside the lines wouldn't hurt.
The example card is for my service technician (Corwin Haldane). If possible I would like to be able to edit the text to use for more than one person.

Industry/Entity Type

Appliance Repair

Contact Information for Business Card

Clean, crisp and professional but needs to be eye catching. Preferably using the black, white and red colour scheme matching the website. Double sided would be nice, but is not necessary.

Colors
ec1f27
ffffff
000000

Requirements
Must have
• Must be able to edit name, phone number and title to use for multiple people. Must show the company website (brasswheelservicing.ca).

```html
<!DOCTYPE html>
<html lang="en">
<head>
<meta charset="utf-8">
<title>Brass Wheel Servicing – Business Card</title>
<link rel="stylesheet" href="https://fonts.googleapis.com/css2?family=Arvo:wght@400;700&display=swap">
<style>
  :root {
    --brand-red: #ec1f27;
    --brand-white: #ffffff;
    --brand-black: #000000;
    --card-black: #050505;
    --stage: #2b2b2b;
    --figure-tone: #2a2a2a;
  }
  * { margin: 0; padding: 0; box-sizing: border-box; }
  html, body {
    width: 1200px; height: 880px; overflow: hidden;
    background: var(--stage);
    font-family: "Arvo", "Rockwell", serif;
  }
  .canvas { position: relative; width: 1200px; height: 880px; }
  .card {
    position: absolute; width: 560px; height: 320px;
    background: var(--card-black); border-radius: 18px; overflow: hidden;
    color: var(--brand-white);
    box-shadow: 0 14px 30px rgba(0,0,0,.45);
  }
  .card--back { left: 60px; top: 60px; }
  .card--front { left: 580px; top: 500px; }

  .brand-mark {
    position: absolute; display: flex; flex-direction: column; align-items: center;
    z-index: 1;
  }
  .brand-mark__figure {
    width: 120px; height: 120px; border-radius: 10px;
    background: linear-gradient(160deg, #333 0%, var(--figure-tone) 60%, #1a1a1a 100%);
  }
  .brand-mark__name {
    margin-top: 8px; font-weight: 700; font-size: 20px; color: var(--brand-white);
    letter-spacing: .5px; white-space: nowrap; line-height: 1.2;
  }
  .card--back .brand-mark { left: 50%; top: 40px; transform: translateX(-50%); }
  .tagline {
    position: absolute; left: 0; right: 0; bottom: 44px; text-align: center;
    font-size: 15px; letter-spacing: .2px;
  }

  .card--front .brand-mark { right: 40px; top: 18px; }
  .card--front .brand-mark__figure { width: 100px; height: 100px; }
  .card--front .brand-mark__name { font-size: 18px; margin-top: 6px; }

  .company-name {
    position: absolute; left: 30px; top: 38px;
    font-weight: 700; font-size: 27px; font-variant: small-caps; letter-spacing: 1px;
    line-height: 1.2;
  }
  .person { position: absolute; left: 34px; top: 88px; }
  .person__name { font-size: 20px; line-height: 1.15; }
  .person__title { font-size: 14px; line-height: 1.2; color: var(--brand-red); }
  .address { position: absolute; left: 34px; top: 140px; font-size: 13px; line-height: 1.35; font-style: normal; }
  .contacts { position: absolute; left: 34px; top: 180px; font-size: 13px; line-height: 1.35; }
  .contacts dt { color: var(--brand-red); display: inline; }
  .contacts dd { display: inline; }
  .contacts dd::after { content: ""; display: block; }
  .swoosh { position: absolute; inset: 0; }
  .website { font-size: 14px; fill: var(--brand-white); }
</style>
</head>
<body>
<main class="canvas">

  <section class="card card--back" aria-label="Card back">
    <div class="brand-mark">
      <div class="brand-mark__figure" role="img" aria-label="Illustration of a technician in a hard hat holding a wrench"></div>
      <span class="brand-mark__name">Brass Wheel</span>
    </div>
    <p class="tagline">when your equipment can’t finish the workout, give us a call !</p>
  </section>

  <section class="card card--front" aria-label="Card front">
    <svg class="swoosh" viewBox="0 0 560 320" width="560" height="320">
      <path d="M0,306 Q300,296 560,170 L560,320 L0,320 Z" fill="var(--brand-white)"/>
      <path d="M0,318 Q300,310 560,186 L560,320 L0,320 Z" fill="var(--brand-red)"/>
      <path id="web-path" d="M250,308 Q400,285 540,212" fill="none"/>
      <text class="website"><textPath href="#web-path">www.brasswheelservicing.ca</textPath></text>
    </svg>

    <h1 class="company-name">Brass Wheel Servicing</h1>

    <div class="person">
      <p class="person__name">Corwin Haldane</p>
      <p class="person__title">service technician</p>
    </div>

    <address class="address">
      815 Larkfield Crescent NW<br>
      Edmonton AB T5X 2K9
    </address>

    <dl class="contacts">
      <dt>Personal:</dt> <dd>578-555-0143</dd>
      <dt>Service Line:</dt> <dd>780-555-0198</dd>
      <dt>Service Email:</dt> <dd>service@brasswheelservicing.ca</dd>
    </dl>

    <div class="brand-mark">
      <div class="brand-mark__figure" role="img" aria-label="Illustration of a technician in a hard hat holding a wrench"></div>
      <span class="brand-mark__name">Brass Wheel</span>
    </div>
  </section>

</main>
</body>
</html>
```